pasmuro.com

Develop a website for pasmura.com will be a site to sell tickets for concerts, shows, shows, theaters and others. I need a web design easy view, very easy to use and accumulate events by date. The aim is to develop the site was connected to a complex system that is already developed. (Important this page to a robust system was connected via links the idea is to develop only the front view)
Updates

Reason: I need more designs yet we have not made the decision

Target Market(s)

millennials, adults, who want to enjoy concerts and shows

Industry/Entity Type

Event

Number of Pages Required

5+ page

Colors
1b1b1b
aaaaaa
ffffff

Requirements
Must have
• Easy Vista, accumulation of upcoming events, past events. The tabs should have are: 1 Start: In this part of upcoming events occur. You could put a banner on the top and down the events by date. 2. How to order: page with instructions on how to purchase tickets 3. About Us: The company history 4. Contact: Phones and template for contact by mail 5. Our policies: shopping 6. Notice Privacy: Privacy Notice Copoy 7. Centers Sale: physical places where they can purchase tickets Promoters 8. access: Link to a template
Nice to have
• as you can see p www.volandrimexa.com or crunvía.com or crunvea.com or plovindex.com (important this page to a robust system was connected via links the idea is to develop only the front view)
Should not have
• Many things Tangled

```html
<!DOCTYPE html>
<html lang="en">
<head>
<meta charset="utf-8">
<title>Pasmuro — Tickets for concerts and shows</title>
<link href="https://fonts.googleapis.com/css2?family=Open+Sans:wght@400;600;700;800&display=swap" rel="stylesheet">
<style>
:root{
  --ink:#1b1b1b;
  --grey:#aaaaaa;
  --white:#ffffff;
  --red:#e0504a;
  --wine:#1e0c14;
  --wine-dark:#140810;
  --footer:#161212;
  --line:rgba(255,255,255,.35);
}
*{box-sizing:border-box;margin:0;padding:0}
html,body{width:718px;height:1200px;overflow:hidden;background:var(--wine-dark)}
body{position:relative;font-family:"Open Sans",Arial,sans-serif;color:var(--white)}
.abs{position:absolute}

/* header */
.site-header{left:0;top:0;width:718px;height:67px;background:linear-gradient(90deg,#1a0a12,#2a0f1b 60%,#1a0a12)}
.brand{display:flex;align-items:center;gap:7px;color:var(--white);font-weight:800;font-size:15px;letter-spacing:.5px;line-height:1}
.brand .mark{width:14px;height:14px;background:var(--red)}
.header-brand{left:52px;top:26px}
.select{display:flex;align-items:center;justify-content:space-between;padding:0 9px;height:24px;background:var(--white);color:var(--ink);font-size:8px;border-radius:2px}
.select::after{content:"";border-left:3.5px solid transparent;border-right:3.5px solid transparent;border-top:4px solid var(--ink)}
.btn-cardboard{left:462px;top:21px;width:102px;height:24px;background:var(--red);font-size:9.5px;font-weight:600;display:flex;align-items:center;justify-content:center;border-radius:2px}
.social{display:flex;gap:6px}
.social span{display:block;width:15px;height:15px;border-radius:2px;background:var(--grey)}
.header-social{left:582px;top:24px}

/* nav */
.main-nav{left:0;top:67px;width:718px;height:35px;background:linear-gradient(#1e1e1e,#111)}
.main-nav a{position:absolute;top:0;height:35px;line-height:35px;font-size:9.5px;color:var(--white);text-decoration:none}
.main-nav a.active{background:#000;border-top:2px solid var(--red);line-height:33px;text-align:center}

/* hero */
.hero{left:0;top:102px;width:718px;height:294px;background:radial-gradient(ellipse at 50% 45%,#4a2a2c 0%,#2e1618 60%,#1e0e10 100%)}
.hero-title{left:0;top:200px;width:718px;text-align:center;font-size:35px;font-weight:800;letter-spacing:.5px}
.hero-sub{left:0;top:243px;width:718px;text-align:center;font-size:19px;font-weight:400}
.round-arrow{width:16px;height:16px;border-radius:50%;background:rgba(0,0,0,.5);border:1px solid rgba(255,255,255,.25)}

/* sections */
.content-bg{left:0;top:396px;width:718px;height:630px;background:radial-gradient(ellipse at 50% 40%,#2c0f1c,transparent 70%),var(--wine)}
.section-title{font-size:17.5px;font-weight:600;letter-spacing:.2px}
.rule{height:1px;background:var(--line)}
.location-label{left:441px;top:456px;font-size:11px;font-weight:600}
.location-select{left:558px;top:451px;width:103px;height:24px;background:transparent;color:var(--white);border:1px solid var(--white)}
.location-select::after{border-top-color:var(--white)}

.poster{width:145px;height:185px;top:501px}
.poster .photo{width:145px;height:185px}
.poster .caption{position:absolute;left:0;bottom:0;width:145px;height:36px;background:rgba(0,0,0,.55);text-align:center;padding-top:6px}
.caption h3{font-size:8.5px;font-weight:600}
.caption p{font-size:7px;color:#ddd;margin-top:1px}

.arrow-pair{left:638px;top:748px}

.event{top:795px;width:199px;height:186px;background:#111}
.event .photo{width:199px;height:143px}
.event .info{position:absolute;left:0;top:143px;width:199px;height:43px;background:rgba(0,0,0,.85)}
.date{position:absolute;left:0;top:0;width:32px;height:43px;background:var(--red);font-size:7.5px;text-align:center;line-height:11px;padding-top:5px}
.event h3{position:absolute;left:38px;top:8px;font-size:9.5px;font-weight:600;width:90px;border-bottom:1px solid var(--white);padding-bottom:1px}
.event p{position:absolute;left:38px;top:24px;font-size:7.5px;color:#ddd}
.book{position:absolute;right:7px;top:10px;width:51px;height:13px;border:1px solid var(--white);border-radius:7px;font-size:6px;text-align:center;line-height:11px}

/* footer */
.site-footer{left:0;top:1026px;width:718px;height:174px;background:var(--footer)}
.footer-brand{left:53px;top:1093px}
.footer-head{font-size:9px;font-weight:400}
.footer-text{font-size:7.5px;line-height:13px;color:#e8e8e8}
.mail-form{left:384px;top:1108px;display:flex}
.mail-form .field{width:88px;height:18px;background:var(--white);color:#999;font-size:6.5px;padding:5px 5px}
.mail-form .submit{width:34px;height:18px;background:#666;font-size:6.5px;text-align:center;line-height:18px}
.footer-social span{width:16px;height:16px;background:var(--white);border-radius:3px}
.copyright{left:0;top:1175px;width:718px;text-align:center;font-size:7.5px}
</style>
</head>
<body>

<header class="site-header abs">
  <div class="brand header-brand abs"><span class="mark"></span><span>PASMURO</span></div>
  <div class="select abs" style="left:236px;top:21px;width:102px">CDMX Center</div>
  <div class="select abs" style="left:349px;top:21px;width:102px">Select a cinema</div>
  <div class="btn-cardboard abs">SEE CARDBOARD</div>
  <div class="social header-social abs" aria-label="Social links">
    <span></span><span></span><span></span><span></span>
  </div>
</header>

<nav class="main-nav abs">
  <a class="active" href="#" style="left:54px;width:68px">HOME</a>
  <a href="#" style="left:130px">HOW TO ORDER</a>
  <a href="#" style="left:231px">ABOUT US</a>
  <a href="#" style="left:306px">CONTACT US</a>
  <a href="#" style="left:393px">POLICIES</a>
  <a href="#" style="left:462px">PRIVACY</a>
  <a href="#" style="left:528px">CENTER SALE</a>
  <a href="#" style="left:615px">ACCESS</a>
</nav>

<section class="hero abs" role="img" aria-label="Photograph of a theatre stage"></section>
<h1 class="hero-title abs">PASMURO SYSTEM</h1>
<p class="hero-sub abs">quisquam est qui dolorem ipsum</p>
<div class="round-arrow abs" style="left:628px;top:362px"></div>
<div class="round-arrow abs" style="left:648px;top:362px"></div>
<svg class="abs" style="left:628px;top:362px" width="36" height="16" viewBox="0 0 36 16" fill="none" stroke="#fff" stroke-width="1.3"><path d="M9.5 5 6.5 8l3 3M26.5 5l3 3-3 3"/></svg>

<div class="content-bg abs"></div>

<h2 class="section-title abs" style="left:55px;top:452px">POSTER IN CDMX CENTER</h2>
<span class="location-label abs">Change your location</span>
<div class="select location-select abs">CDMX Center</div>
<div class="rule abs" style="left:52px;top:488px;width:611px"></div>

<article class="poster abs" style="left:52px">
  <div class="photo" role="img" aria-label="Concert crowd under red confetti" style="background:linear-gradient(#8a1a1e,#3a0b10 70%,#150507)"></div>
  <div class="caption"><h3>QUISQUAM EST QUI</h3><p>Ipsum quia dolor sit</p></div>
</article>
<article class="poster abs" style="left:206px">
  <div class="photo" role="img" aria-label="Two guitarists playing on a blue-lit stage" style="background:linear-gradient(#2f5f78,#16303e 60%,#0b1820)"></div>
  <div class="caption"><h3>QUISQUAM EST QUI</h3><p>Ipsum quia dolor sit</p></div>
</article>
<article class="poster abs" style="left:360px">
  <div class="photo" role="img" aria-label="Theatre hall with red seats" style="background:linear-gradient(135deg,#1f5fb0,#5a7fb0 45%,#7a2a40 80%,#b01e40)"></div>
  <div class="caption"><h3>QUISQUAM EST QUI</h3><p>Ipsum quia dolor sit</p></div>
</article>
<article class="poster abs" style="left:514px">
  <div class="photo" role="img" aria-label="Juggling performer in a colourful costume" style="background:linear-gradient(#2a1c30,#7a3a8a 50%,#b04a70)"></div>
  <div class="caption"><h3>QUISQUAM EST QUI</h3><p>Ipsum quia dolor sit</p></div>
</article>

<h2 class="section-title abs" style="left:53px;top:746px">UPCOMING EVENTS</h2>
<svg class="arrow-pair abs" width="22" height="14" viewBox="0 0 22 14" fill="none" stroke="#fff" stroke-width="2"><path d="M7 2 2 7l5 5M15 2l5 5-5 5"/></svg>
<div class="rule abs" style="left:53px;top:777px;width:612px"></div>

<article class="event abs" style="left:53px">
  <div class="photo" role="img" aria-label="Band performing under stage lights" style="background:linear-gradient(#1a1e2e,#34405e 60%,#1a2440)"></div>
  <div class="info"><div class="date">1<br>NOV<br>2017</div><h3>NEQUE PORRO</h3><p>Dolorem ipsum quia dolor</p><div class="book">BOOK NOW</div></div>
</article>
<article class="event abs" style="left:260px">
  <div class="photo" role="img" aria-label="Concert crowd in warm orange light" style="background:radial-gradient(ellipse at 60% 25%,#e09040,#8a3a14 50%,#2a0e06)"></div>
  <div class="info"><div class="date">2<br>NOV<br>2017</div><h3>NEQUE PORRO</h3><p>Dolorem ipsum quia dolor</p><div class="book">BOOK NOW</div></div>
</article>
<article class="event abs" style="left:466px">
  <div class="photo" role="img" aria-label="Guitar being played in pink light" style="background:linear-gradient(120deg,#3a1a30,#8a3a6a 50%,#c07090)"></div>
  <div class="info"><div class="date">2<br>NOV<br>2017</div><h3>NEQUE PORRO</h3><p>Dolorem ipsum quia dolor</p><div class="book">BOOK NOW</div></div>
</article>

<footer class="site-footer abs"></footer>
<div class="brand footer-brand abs"><span class="mark"></span><span>PASMURO</span></div>

<h4 class="footer-head abs" style="left:205px;top:1061px">CONTACT US</h4>
<p class="footer-text abs" style="left:206px;top:1083px">Address : 2716 Corvella Ave,<br>Lindmoor, Fl, 33190<br>Phone : 555-014-2278<br>Email : hello@pasmuro.com</p>

<h4 class="footer-head abs" style="left:384px;top:1061px">JOIN OUR MAILING LIST</h4>
<p class="footer-text abs" style="left:384px;top:1082px;font-size:6.5px;line-height:10px">Your about us information would fit<br>here nicely.</p>
<div class="mail-form abs"><div class="field">Email address</div><div class="submit">Submit</div></div>

<h4 class="footer-head abs" style="left:563px;top:1061px">FOLLOW US OUT THERE</h4>
<div class="social footer-social abs" style="left:563px;top:1087px;gap:7px" aria-label="Social links">
  <span></span><span></span><span></span><span></span>
</div>

<div class="rule abs" style="left:45px;top:1160px;width:612px;background:rgba(255,255,255,.15)"></div>
<p class="copyright abs">Copyright © 2017. All Rights Reserved</p>

</body>
</html>
```